Package design for Mica powder sachets

Our mica powder product comes in two sets of colors, a set of 60 and 35 packed inside sachet bags individually. This project will require two sizes of the packing box , one for the set of 60 and other for 35. We do not have a specific design requirement as long as the design reflects the theme of our product. Box diagram for both sizes is attached together with color chart, content, logo, sachet design and sample of a packaging design we like. The content is the same for both sizes accept for number of colors included.

```html
<!DOCTYPE html>
<html lang="en">
<head>
<meta charset="utf-8">
<title>Aspen Crafts – 60 Mica Powder Box Dieline</title>
<link href="https://fonts.googleapis.com/css2?family=Oswald:wght@400;500;600&family=Tinos:wght@700&family=Arimo:wght@400&display=swap" rel="stylesheet">
<style>
  :root{
    --paper:#ffffff;
    --ink:#000000;
    --white:#ffffff;
    --tag-yellow:#e8f03c;
    --ribbon-pink:#ee1a7a;
    --badge-lime:#c8f000;
    --badge-dark:#5a8a00;
  }
  *{box-sizing:border-box;margin:0;padding:0}
  html,body{width:1200px;height:1200px;overflow:hidden;background:var(--paper)}
  .canvas{position:relative;width:1200px;height:1200px;background:var(--paper);font-family:'Oswald',sans-serif;color:var(--white)}
  .dieline{position:absolute;left:0;top:0}
  .panel{position:absolute;overflow:hidden}
  .flip{transform:rotate(180deg)}

  .brand{position:absolute;text-align:center;font-family:'Oswald',sans-serif;font-weight:600;color:var(--white);line-height:1}
  .brand .word{display:block}

  .splash{position:absolute;
    background:
      radial-gradient(ellipse 40% 35% at 60% 55%, rgba(255,80,170,.95), transparent 70%),
      radial-gradient(ellipse 35% 30% at 30% 75%, rgba(32,200,232,.85), transparent 70%),
      radial-gradient(ellipse 40% 35% at 40% 30%, rgba(138,43,226,.8), transparent 70%),
      radial-gradient(ellipse 30% 25% at 75% 80%, rgba(42,92,255,.75), transparent 70%),
      radial-gradient(ellipse 55% 50% at 50% 50%, rgba(255,255,255,.25), transparent 75%);
  }

  .tagline{position:absolute;white-space:nowrap;font-family:'Oswald',sans-serif;font-weight:500;color:var(--tag-yellow);letter-spacing:-.01em}
  .tagline .dot{display:inline-block;width:.38em;height:.38em;background:var(--tag-yellow);margin:0 .25em .15em .25em;vertical-align:middle}

  .badge{position:absolute;border-radius:50%;
    background:radial-gradient(circle at 40% 35%, #f6ff9a 0%, var(--badge-lime) 45%, var(--badge-dark) 100%);
    display:flex;align-items:center;justify-content:center;
    font-family:'Tinos',serif;font-weight:700;color:#111}
  .ribbon{position:absolute;background:var(--ribbon-pink);font-family:'Tinos',serif;font-weight:700;color:var(--white);line-height:1.05;text-transform:uppercase}

  .uses{position:absolute;font-family:'Arimo',sans-serif;font-size:11.5px;line-height:14px;color:var(--white)}

  .address{position:absolute;font-family:'Oswald',sans-serif;font-size:9.5px;line-height:12.5px;font-weight:400;white-space:nowrap}
  .chart{position:absolute;left:42px;top:132px;display:grid;grid-template-columns:89px 92px 85px 80px 79px 100px;grid-auto-flow:column;grid-template-rows:repeat(10,17.1px)}
  .chip{display:flex;align-items:center;font-family:'Oswald',sans-serif;font-size:6.6px;white-space:nowrap;letter-spacing:.01em}
  .chip i{display:inline-block;width:10px;height:10px;margin-right:4px;flex:none}
  .contents{position:absolute;font-family:'Oswald',sans-serif;font-weight:500;white-space:nowrap;line-height:1}
  .warning{position:absolute;left:373px;top:312px;width:91px;height:47px;background:var(--white);color:var(--ink);font-family:'Arimo',sans-serif;padding:3px 5px;font-size:6px;line-height:7.5px}
  .warning .head{display:flex;align-items:center;gap:3px;font-family:'Oswald',sans-serif;font-weight:600;font-size:11px;line-height:12px}

  .serif-line{position:absolute;font-family:'Tinos',serif;font-weight:700;text-transform:uppercase;line-height:1;color:var(--white)}
  .vertical{position:absolute;transform-origin:center}
</style>
</head>
<body>
<div class="canvas">

  <svg class="dieline" width="1200" height="1200" viewBox="0 0 1200 1200" aria-hidden="true">
    <g fill="#000">
      <path d="M178,159 L178,130 Q178,34 280,34 L926,34 Q1028,34 1028,130 L1028,159 Z"/>
      <rect x="178" y="159" width="850" height="3"/>
      <rect x="322" y="159" width="569" height="381"/>
      <path d="M322,162 L231,197 Q178,205 178,240 L178,470 Q178,495 231,500 L322,537 Z"/>
      <path d="M891,162 L982,197 Q1028,205 1028,240 L1028,470 Q1028,495 982,500 L891,537 Z"/>
      <rect x="178" y="540" width="850" height="118"/>
      <rect x="319" y="658" width="572" height="517"/>
      <rect x="39" y="666" width="278" height="381"/>
      <rect x="39" y="1054" width="278" height="120"/>
      <rect x="891" y="664" width="277" height="381"/>
      <rect x="891" y="1054" width="277" height="120"/>
    </g>
  </svg>

  <!-- LID (printed upside down) -->
  <section class="panel lid flip" style="left:322px;top:159px;width:569px;height:381px">
    <div class="splash" role="img" aria-label="Burst of colourful mica powder in pink, violet and cyan" style="left:177px;top:3px;width:160px;height:93px"></div>
    <div class="brand" style="left:40px;top:20px;width:150px">
      <span class="word" style="font-size:38px">Aspen</span>
      <span class="word" style="font-size:18px;letter-spacing:.45em;margin-top:8px;padding-left:.45em">CRAFTS</span>
    </div>
    <div class="address" style="left:371px;top:25px">YOUR COMPANY NAME<br>ADDRESS: XOLLOXLOXLOXLOXL<br>XLOXLOXLXOXLXOXLXOL<br>PHONE:0123450000</div>
    <div class="tagline" style="left:43px;top:92px;font-size:13px">
      <span class="dot"></span>MULTI-PURPOSE<span class="dot"></span>COSMETIC GRADE<span class="dot"></span>NON-TOXIC<span class="dot"></span>PREMIUM COLORS
    </div>

    <div class="chart">
      <span class="chip"><i style="background:#3fc9a5"></i>M1 WINDY BLUE</span>
      <span class="chip"><i style="background:#53e0a8"></i>M2 SAGE GLOW</span>
      <span class="chip"><i style="background:#d97a7a"></i>M2 PEACH BLOSSOM</span>
      <span class="chip"><i style="background:#f4a838"></i>M5 GOLD GLOW</span>
      <span class="chip"><i style="background:#d4d4d4"></i>M6 PEARL WHITE</span>
      <span class="chip"><i style="background:#e6a94a"></i>M7 LIGHT GOLD</span>
      <span class="chip"><i style="background:#fbc72a"></i>M9 YELLOW GOLD</span>
      <span class="chip"><i style="background:#c8a45a"></i>M12 CLASSIC GOLD</span>
      <span class="chip"><i style="background:#e3a34a"></i>M13 GLITZY GOLD</span>
      <span class="chip"><i style="background:#fbe21a"></i>M15 TUSCANY YELLOW</span>

      <span class="chip"><i style="background:#8aa07a"></i>M16 CITRUS ZEST</span>
      <span class="chip"><i style="background:#f2ea2a"></i>M18 LEMON TWIST</span>
      <span class="chip"><i style="background:#4c6270"></i>M20 RAVEN GRAY</span>
      <span class="chip"><i style="background:#4a4a66"></i>M21 CHARCOAL</span>
      <span class="chip"><i style="background:#6a7a7a"></i>M22 SPACE GRAY</span>
      <span class="chip"><i style="background:#8a1030"></i>M23 CHOCOLATE BROWN</span>
      <span class="chip"><i style="background:#b8c0d0"></i>M24 BRONZE</span>
      <span class="chip"><i style="background:#8a0a12"></i>M26 MOCHA BROWN</span>
      <span class="chip"><i style="background:#b8882a"></i>M27 GOLDEN BROWN</span>
      <span class="chip"><i style="background:#3c8a3c"></i>M29 JUNGLE GREEN</span>

      <span class="chip"><i style="background:#3a9a5a"></i>M30 SEA GREEN</span>
      <span class="chip"><i style="background:#2a9a72"></i>M31 TURQUOISE</span>
      <span class="chip"><i style="background:#6ab84a"></i>M32 MINT GREEN</span>
      <span class="chip"><i style="background:#2e8a4a"></i>M34 HUNTER GREEN</span>
      <span class="chip"><i style="background:#4a6a3a"></i>M35 EMERALD GREEN</span>
      <span class="chip"><i style="background:#a8c83a"></i>M36 SPRING GREEN</span>
      <span class="chip"><i style="background:#3a8a4a"></i>M38 FOREST GREEN</span>
      <span class="chip"><i style="background:#2a9ab0"></i>M40 SKY BLUE</span>
      <span class="chip"><i style="background:#1a6ad0"></i>M42 MARLIN BLUE</span>
      <span class="chip"><i style="background:#1a3a7a"></i>M43 DENIM BLUE</span>

      <span class="chip"><i style="background:#2a9ac8"></i>M44 WHALE BLUE</span>
      <span class="chip"><i style="background:#30a8c0"></i>M45 BRIGHT BLUE</span>
      <span class="chip"><i style="background:#1a3aa0"></i>M47 SAPPHIRE BLUE</span>
      <span class="chip"><i style="background:#3aa8c8"></i>M48 OCEAN BLUE</span>
      <span class="chip"><i style="background:#1a2a5a"></i>M49 NAVY BLUE</span>
      <span class="chip"><i style="background:#1a3a8a"></i>M50 ROYAL PURPLE</span>
      <span class="chip"><i style="background:#5a2a7a"></i>M53 VIOLET PURPLE</span>
      <span class="chip"><i style="background:#5a2a3a"></i>M54 IRIS</span>
      <span class="chip"><i style="background:#f4c8c8"></i>M55 LAVINDER</span>
      <span class="chip"><i style="background:#7a3a8a"></i>M56 DUSK PURPLE</span>

      <span class="chip"><i style="background:#e05a1a"></i>M57 CORAL ORANGE</span>
      <span class="chip"><i style="background:#e8641a"></i>M58 NEON ORANGE</span>
      <span class="chip"><i style="background:#c8101a"></i>M59 ROSE RED</span>
      <span class="chip"><i style="background:#b84a4a"></i>M60 CRIMSON RED</span>
      <span class="chip"><i style="background:#b80a1a"></i>M61 RUBY</span>
      <span class="chip"><i style="background:#c81020"></i>M62 RASPBERRY</span>
      <span class="chip"><i style="background:#e0106a"></i>M65 MAGENTA</span>
      <span class="chip"><i style="background:#e04a8a"></i>M67 ROSE PINK</span>
      <span class="chip"><i style="background:#6a0a1a"></i>M69 MAROON</span>
      <span class="chip"><i style="background:#a00a1a"></i>M68 MAHOGANY</span>

      <span class="chip"><i style="background:#e80a6a"></i>M70 HOT PINK</span>
      <span class="chip"><i style="background:#9a5a4a"></i>M72 LILAC</span>
      <span class="chip"><i style="background:#e8a88a"></i>M73 CREAMY PINK</span>
      <span class="chip"><i style="background:#7a0a1a"></i>M74 BURGANDY</span>
      <span class="chip"><i style="background:#b85a1a"></i>M75 COPPER</span>
      <span class="chip"><i style="background:#c8b8a8"></i>M76 BRONZE GOLD</span>
      <span class="chip"><i style="background:#8a0a10"></i>M77 BURNT ORANGE</span>
      <span class="chip"><i style="background:#e0eef4"></i>M78 BRILLIANT SILVER</span>
      <span class="chip"><i style="background:#6a7a4a"></i>M79 PEWTER</span>
      <span class="chip"><i style="background:#5a6a3a"></i>M80 OLIVE GREEN</span>
    </div>

    <div class="contents" style="left:175px;top:296px;font-size:14px">CONTENTS: 60 COLORS,</div>
    <div class="contents" style="left:237px;top:313px;font-size:14px">3 MEASURING SPOONS,</div>
    <div class="contents" style="left:236px;top:328px;font-size:13px">USER GUIDE</div>
    <div class="contents" style="left:175px;top:343px;font-size:8.5px;font-weight:400">PLEASE VISIT WWW.SHOPASPENCRAFTS.COM</div>
    <div class="contents" style="left:175px;top:354px;font-size:8.5px;font-weight:400">FOR MORE PRODUCTS ANDAND INFORMATION</div>

    <div class="warning">
      <div class="head">
        <svg width="12" height="11" viewBox="0 0 12 11" aria-hidden="true"><path d="M6,0.5 L11.5,10.5 L0.5,10.5 Z" fill="#f2d400" stroke="#000" stroke-width="0.8"/><rect x="5.4" y="3.5" width="1.2" height="4" fill="#000"/><rect x="5.4" y="8.2" width="1.2" height="1.2" fill="#000"/></svg>
        WARNING
      </div>
      CHOKING HAZARD<br>SMALL PARTS. NOT FOR<br>CHILDREN UNDER 3 YEARS
    </div>
  </section>

  <!-- BACK PANEL (printed upside down) -->
  <section class="panel back flip" style="left:319px;top:540px;width:572px;height:118px">
    <div class="splash" role="img" aria-label="Burst of colourful mica powder in pink, violet and cyan" style="left:244px;top:0;width:131px;height:74px"></div>
    <div class="brand" style="left:72px;top:14px;width:175px">
      <span class="word" style="font-size:40px">Aspen</span>
      <span class="word" style="font-size:19px;letter-spacing:.45em;margin-top:10px;padding-left:.45em">CRAFTS</span>
    </div>
    <div class="serif-line" style="left:350px;top:33px;font-size:18px;line-height:18px">Inspiring<br>Mica Powder<br>Colors</div>
  </section>

  <!-- FRONT PANEL -->
  <section class="panel front" style="left:319px;top:658px;width:572px;height:517px">
    <div class="splash" role="img" aria-label="Large burst of colourful mica powder in pink, magenta, violet, blue and cyan" style="left:31px;top:29px;width:457px;height:482px"></div>
    <div class="brand" style="left:141px;top:44px;width:284px">
      <span class="word" style="font-size:84px;letter-spacing:.02em">Aspen</span>
      <span class="word" style="font-size:36px;letter-spacing:.5em;margin-top:16px;padding-left:.5em">CRAFTS</span>
    </div>
    <div class="tagline" style="left:84px;top:205px;font-size:16.5px">
      <span class="dot"></span>MULTI-PURPOSE<span class="dot"></span>COSMETIC GRADE<span class="dot"></span>NON-TOXIC<span class="dot"></span>PREMIUM COLORS
    </div>
    <div class="ribbon" style="left:94px;top:301px;width:153px;height:50px;padding:5px 0 0 22px;font-size:13.5px;clip-path:polygon(0 0,100% 0,94% 50%,100% 100%,0 100%)">Inspiring<br>Mica Powder<br>Colors</div>
    <div class="badge" style="left:28px;top:285px;width:76px;height:76px;font-size:44px">60</div>
    <div class="uses" style="left:447px;top:296px">FOR<br>EPOXY RESIN, SOAP<br>SLIME<br>CANDLES<br>PAINT<br>AND MUCH MORE</div>
    <div class="brand" style="left:375px;top:404px;width:172px">
      <span class="word" style="font-size:46px">Aspen</span>
      <span class="word" style="font-size:20px;letter-spacing:.45em;margin-top:10px;padding-left:.45em">CRAFTS</span>
    </div>
  </section>

  <!-- LEFT SIDE PANEL -->
  <section class="panel side-left" style="left:39px;top:666px;width:278px;height:381px">
    <div class="vertical" style="left:120px;top:80px;width:170px;height:86px;transform:rotate(90deg)">
      <div class="brand" style="left:0;top:0;width:170px">
        <span class="word" style="font-size:44px">Aspen</span>
        <span class="word" style="font-size:20px;letter-spacing:.45em;margin-top:10px;padding-left:.45em">CRAFTS</span>
      </div>
    </div>
    <div class="ribbon" style="left:182px;top:259px;width:35px;height:94px;clip-path:polygon(0 0,100% 0,100% 100%,50% 94%,0 100%)"></div>
    <div class="serif-line" style="left:152px;top:293px;width:94px;height:27px;font-size:8.5px;line-height:9px;transform:rotate(90deg)">Inspiring<br>Mica Powder<br>Colors</div>
    <div class="badge" style="left:175px;top:205px;width:52px;height:52px;font-size:30px;transform:rotate(90deg)">60</div>
  </section>

  <!-- RIGHT SIDE PANEL -->
  <section class="panel side-right" style="left:891px;top:664px;width:277px;height:381px">
    <div class="vertical" style="left:-27px;top:243px;width:170px;height:86px;transform:rotate(-90deg)">
      <div class="brand" style="left:0;top:0;width:170px">
        <span class="word" style="font-size:44px">Aspen</span>
        <span class="word" style="font-size:20px;letter-spacing:.45em;margin-top:10px;padding-left:.45em">CRAFTS</span>
      </div>
    </div>
    <div class="ribbon" style="left:50px;top:36px;width:34px;height:100px;clip-path:polygon(0 6%,50% 0,100% 6%,100% 100%,0 100%)"></div>
    <div class="serif-line" style="left:20px;top:73px;width:94px;height:27px;font-size:8.5px;line-height:9px;transform:rotate(-90deg)">Inspiring<br>Mica Powder<br>Colors</div>
    <div class="badge" style="left:40px;top:138px;width:52px;height:52px;font-size:30px;transform:rotate(-90deg)">60</div>
  </section>

</div>
</body>
</html>
```